Business Card Design needed for logo design project

Our company needs a Business Card Design. Please refer to our original project in the link above.

Industry/Entity Type

Business

```html
<!DOCTYPE html>
<html lang="en">
<head>
<meta charset="utf-8">
<title>Nestora Business Card</title>
<link rel="stylesheet" href="https://fonts.googleapis.com/css2?family=ABeeZee&display=swap">
<style>
  :root {
    --page-bg: #e3e1de;
    --card-top: #f9fbfb;
    --card-bottom: #edf3f2;
    --teal-bright: #1fb89e;
    --teal-light: #55c2ad;
    --teal-dark: #2a9b8c;
    --teal-front: #229c84;
    --logo-grey: #6e6e6e;
    --ink: #333333;
    --ink-soft: #454545;
    --rule: #7a7a7a;
    --white: #ffffff;
  }
  * { margin: 0; padding: 0; box-sizing: border-box; }
  html, body {
    width: 1200px;
    height: 685px;
    overflow: hidden;
    background: var(--page-bg);
    font-family: "ABeeZee", Arial, sans-serif;
  }
  .canvas {
    position: relative;
    width: 1200px;
    height: 685px;
  }
  .card {
    position: absolute;
    top: 185px;
    width: 590px;
    height: 332px;
    transform: scale(0.95);
    transform-origin: top left;
    overflow: hidden;
    background: linear-gradient(180deg, var(--card-top), var(--card-bottom));
    box-shadow: 0 6px 18px rgba(0, 0, 0, 0.18);
  }
  .card--front { left: 26px; }
  .card--back  { left: 613px; }
  .card-shapes {
    position: absolute;
    inset: 0;
  }

  /* Front */
  .front-wordmark {
    position: absolute;
    left: 250px;
    top: 136px;
    font-size: 74px;
    line-height: 1;
    color: var(--logo-grey);
    letter-spacing: 1px;
  }

  /* Back */
  .back-wordmark {
    position: absolute;
    left: 30px;
    top: 14px;
    font-size: 46px;
    line-height: 1;
    color: var(--logo-grey);
    letter-spacing: 1px;
  }
  .holder-name {
    position: absolute;
    left: 282px;
    top: 45px;
    font-size: 27px;
    line-height: 1;
    color: var(--white);
  }
  .tagline {
    position: absolute;
    left: 65px;
    top: 168px;
    font-size: 19px;
    line-height: 26px;
    color: var(--ink);
  }
  .contact-list {
    position: absolute;
    left: 345px;
    top: 130px;
    list-style: none;
  }
  .contact-item {
    display: flex;
    align-items: center;
    height: 49px;
    font-size: 13.5px;
    letter-spacing: 1px;
    color: var(--ink-soft);
  }
  .contact-icon {
    width: 22px;
    height: 22px;
    margin-right: 22px;
    fill: var(--ink);
  }
</style>
</head>
<body>
<main class="canvas">

  <section class="card card--front" aria-label="Card front">
    <svg class="card-shapes" viewBox="0 0 590 332" aria-hidden="true">
      <path d="M0 142 L252 142 C205 160 196 218 258 236 L0 236 Z" fill="var(--teal-front)"/>
    </svg>
    <div class="front-wordmark">nestora</div>
  </section>

  <section class="card card--back" aria-label="Card back">
    <svg class="card-shapes" viewBox="0 0 590 332" aria-hidden="true">
      <path d="M0 62 C70 70 150 90 205 74 L205 120 L0 120 Z" fill="var(--teal-bright)"/>
      <polygon points="205,74 248,33 248,96 205,120" fill="var(--teal-light)"/>
      <rect x="248" y="33" width="342" height="63" fill="var(--teal-dark)"/>
      <line x1="250" y1="102" x2="250" y2="332" stroke="var(--rule)" stroke-width="2"/>
    </svg>

    <div class="back-wordmark">nestora</div>
    <div class="holder-name">[First and Last Name]</div>

    <p class="tagline">[Text ........<br>............<br>..............Here]</p>

    <ul class="contact-list">
      <li class="contact-item">
        <svg class="contact-icon" viewBox="0 0 24 24" aria-hidden="true"><path d="M12 3 L1 12 H4 V21 H10 V15 H14 V21 H20 V12 H23 Z"/></svg>
        [Street Adderess]
      </li>
      <li class="contact-item">
        <svg class="contact-icon" viewBox="0 0 24 24" aria-hidden="true"><path d="M6.6 10.8a15 15 0 0 0 6.6 6.6l2.2-2.2c.3-.3.7-.4 1-.2 1.1.4 2.3.6 3.6.6.6 0 1 .4 1 1V20c0 .6-.4 1-1 1A17 17 0 0 1 3 4c0-.6.4-1 1-1h3.5c.6 0 1 .4 1 1 0 1.3.2 2.5.6 3.6.1.3 0 .7-.2 1z"/></svg>
        [Phone Number]
      </li>
      <li class="contact-item">
        <svg class="contact-icon" viewBox="0 0 24 24" aria-hidden="true"><path d="M2 5 H22 V19 H2 Z M3.5 6.5 L12 13 L20.5 6.5 Z" fill-rule="evenodd"/></svg>
        [Email Adderess]
      </li>
      <li class="contact-item">
        <svg class="contact-icon" viewBox="0 0 24 24" aria-hidden="true"><path d="M4 5 H20 V16 H4 Z M5.5 6.5 V14.5 H18.5 V6.5 Z M1 17 H23 V19 H1 Z" fill-rule="evenodd"/></svg>
        [Website]
      </li>
    </ul>
  </section>

</main>
</body>
</html>
```